Packaging Design for High end coffee beans

The name is Cafe de Marvela.

I need this design to be amended you are welcome to design your own too.

We sell high end coffee beans from Colombia this needs to be reflected in the packaging.

The colour is black and Gold. i need the lettering to be fully gold not a fade.

It is to be printed on coffee packaging so the clarity and quality has to be ready for that.

I need Just harvest and Woodland covenant logos added.
Also to be added to the design is:
Single Origin
Traceability
Sustainability

"Awaken you senses" to be added.

I have added some jpegs that i own. you are free to use stock images where appropiate.

Target Market(s)

Coffee Consumers

Requirements
Must have
• Scalable vector files .. whatever images or file design you prodcue mut be able to be printed in high quality
High end quality
Awaken Your Senses needs tl be shown
Logos of just harvest or Wood land covenant to be added
200g weight to be shown
We have 4 beans which need to be shown individually
Velma Nectar
K3 Morandi
Teal Juniper
Altezza Amber
Nice to have
• You are welcome to come up with your own design

```html
<!DOCTYPE html>
<html lang="en">
<head>
<meta charset="utf-8">
<title>Cafe de Marvela — Coffee Pouch</title>
<link rel="stylesheet" href="https://fonts.googleapis.com/css2?family=Marcellus&family=Cormorant+Garamond:wght@500&display=swap">
<style>
  :root {
    --backdrop: #a39f2e;
    --pouch: #0e0e0e;
    --pouch-band: #161616;
    --gold: #d39a1c;
    --ornament: #c8901a;
  }
  * { box-sizing: border-box; margin: 0; padding: 0; }
  html, body { width: 1200px; height: 982px; overflow: hidden; }
  body { background: var(--backdrop); position: relative; }

  .pouch {
    position: absolute;
    width: 268px;
    height: 546px;
    background: var(--pouch);
    border-radius: 6px 6px 2px 2px;
    color: var(--gold);
    font-family: "Marcellus", serif;
    font-weight: 400;
    text-align: center;
    overflow: hidden;
  }
  .pouch--front { left: 306px; top: 234px; }
  .pouch--back  { left: 626px; top: 234px; }

  .pouch__notch {
    position: absolute;
    top: 42px;
    width: 8px; height: 8px;
    border-radius: 50%;
    background: var(--backdrop);
  }
  .pouch__notch--left { left: -4px; }
  .pouch__notch--right { right: -4px; }

  .pouch__band {
    position: absolute;
    left: 0; right: 0;
    background: var(--pouch-band);
  }
  .pouch__band--top { top: 0; height: 52px; }
  .pouch__band--bottom { bottom: 0; height: 44px; }
  .pouch--back .pouch__band--bottom { height: 40px; }

  .brand-mark {
    position: absolute;
    left: 50%;
    transform: translateX(-50%);
    border: 1px solid var(--gold);
    border-radius: 50%;
    display: flex;
    align-items: center;
    justify-content: center;
    color: var(--gold);
    line-height: 1.3;
  }
  .pouch--front .brand-mark { top: 96px; width: 132px; height: 132px; font-size: 15px; letter-spacing: 2px; }
  .pouch--back .brand-mark { top: 62px; width: 70px; height: 70px; font-size: 9px; letter-spacing: 1px; }

  .tagline {
    position: absolute;
    left: 0; right: 0;
    text-transform: uppercase;
    white-space: nowrap;
    font-weight: 400;
  }
  .pouch--front .tagline { top: 264px; font-size: 13px; letter-spacing: 5px; }
  .pouch--back .tagline { top: 142px; font-size: 10px; letter-spacing: 3px; }

  .ornament {
    position: absolute;
    left: 50%;
    top: 388px;
    width: 104px;
    height: 44px;
    transform: translateX(-50%);
    background: var(--ornament);
    border-radius: 4px;
  }

  .product-name {
    position: absolute;
    left: 0; right: 0;
    top: 442px;
    font-size: 14px;
    font-weight: 400;
    letter-spacing: 5px;
    text-transform: uppercase;
  }
  .net-weight {
    position: absolute;
    left: 0; right: 0;
    top: 484px;
    font-size: 7px;
    letter-spacing: 3px;
    text-transform: uppercase;
  }

  .story {
    position: absolute;
    left: 18px; right: 14px;
    top: 166px;
    font-family: "Cormorant Garamond", serif;
    font-weight: 500;
    font-size: 13px;
    line-height: 16px;
    letter-spacing: 0.4px;
  }

  .contact {
    position: absolute;
    left: 0; right: 0;
    top: 396px;
    display: flex;
    flex-direction: column;
    gap: 4px;
  }
  .contact__name { font-size: 12px; letter-spacing: 3px; }
  .contact__phone { font-size: 9px; letter-spacing: 1px; }
  .contact__web { font-size: 7px; letter-spacing: 4px; }

  .certifications {
    position: absolute;
    left: 0; right: 0;
    top: 446px;
    display: flex;
    justify-content: center;
    gap: 26px;
  }
  .cert-badge {
    width: 28px; height: 28px;
    border-radius: 50%;
    background: var(--gold);
  }

  .origin-note {
    position: absolute;
    left: 0; right: 0;
    top: 482px;
    font-size: 5.5px;
    letter-spacing: 1.6px;
    line-height: 8px;
    text-transform: uppercase;
  }
</style>
</head>
<body>

  <section class="pouch pouch--front">
    <span class="pouch__notch pouch__notch--left"></span>
    <span class="pouch__notch pouch__notch--right"></span>
    <div class="pouch__band pouch__band--top" role="img" aria-label="Tone-on-tone black geometric Colombian pattern band"></div>

    <div class="brand-mark">Cafe de<br>Marvela</div>

    <p class="tagline">Awaken Your Senses</p>

    <div class="ornament" role="img" aria-label="Gold pre-Columbian style geometric ornament"></div>

    <h1 class="product-name">Altezza Amber</h1>
    <p class="net-weight">Net wt 200g</p>

    <div class="pouch__band pouch__band--bottom" role="img" aria-label="Tone-on-tone black geometric Colombian pattern band"></div>
  </section>

  <section class="pouch pouch--back">
    <span class="pouch__notch pouch__notch--left"></span>
    <span class="pouch__notch pouch__notch--right"></span>
    <div class="pouch__band pouch__band--top" role="img" aria-label="Tone-on-tone black geometric Colombian pattern band"></div>

    <div class="brand-mark">Cafe de<br>Marvela</div>

    <p class="tagline">Awaken Your Senses</p>

    <p class="story">
      Our Colombian coffee mountains are giving birth to our coffee beans, the beans are born in coffee families. That have generations of tradition in producing coffee. It is this passion, love and dedication that our coffee families give day to day to each process and step to make the best coffee.
      You are not only sipping on the finest coffee you are also experiencing a journey into the Colombian culture.
    </p>

    <div class="contact">
      <p class="contact__name">Café De Marvela</p>
      <p class="contact__phone">Tel: 0203 555 0148</p>
      <p class="contact__web">www.marvelacafe.com</p>
    </div>

    <div class="certifications">
      <span class="cert-badge" role="img" aria-label="Just harvest certification badge"></span>
      <span class="cert-badge" role="img" aria-label="Woodland covenant certification badge"></span>
    </div>

    <p class="origin-note">Single origin Colombian coffee beans<br>Roasted and packed in the United Kingdom</p>

    <div class="pouch__band pouch__band--bottom" role="img" aria-label="Tone-on-tone black geometric Colombian pattern band"></div>
  </section>

</body>
</html>
```